Creative Report - A Presentation

We are looking for a report to visual workers' compensation claim data and the impact claims have on premium. I’m looking for something that is very visually new, appealing, easy to understand, and cutting edge.

Right now we are looking for 6 pages to be designed: a cover page, an informative page, and 4 reports. The key data for the last 3 reports are listed in the other document attached named “Key Data for Report”. These should be designed in a 8.5 x 11 page layout.

I would prefer a way where things can be combined without looking too crowded. You can play around with the background, for printing purposes try to leave white space.

Attached are a few graphs that I found that I like the look of. Please design when YOU think is best. The docx & the comments on the side are just to help you visualize.

We are a mod analysis company that is always developing new reports. We are hoping to find a designer we can work with in the future as well – think of this as a trial run!

2 designers reached out this morning wanting to submit designs, I would like to see what they have.

```html
<!DOCTYPE html>
<html lang="en">
<head>
<meta charset="utf-8">
<title>Workers Compensation Executive Summary – Report Pages</title>
<link rel="stylesheet" href="https://fonts.googleapis.com/css2?family=Montserrat:wght@400;500;600;700;800&family=Poppins:wght@600;700&display=swap">
<style>
  :root{
    --navy:#0b1f63;
    --ink:#1e1e1e;
    --gold:#f9ab25;
    --backdrop:#d9d9d9;
    --panel:#efefef;
    --rule:#c9c9c9;
    --text:#3a3a3a;
    --white:#ffffff;
  }
  *{box-sizing:border-box;margin:0;padding:0}
  html,body{width:1200px;height:2400px;overflow:hidden}
  body{background:var(--backdrop);font-family:"Montserrat",Arial,sans-serif;color:var(--text);position:relative}
  .page{position:absolute;left:323px;width:559px;height:723px;background:var(--white);box-shadow:0 4px 14px rgba(0,0,0,.12);overflow:hidden}
  .page--cover{top:88px;background:linear-gradient(160deg,#e6e6e6 0%,#f6f6f6 30%,#ffffff 55%)}
  .page--intro{top:846px}
  .page--mod{top:1614px}
  .footer-band{position:absolute;left:0;right:0;bottom:0;height:9px;background:var(--navy)}

  /* brand lockup */
  .brand{position:absolute;display:flex;align-items:center;gap:10px}
  .brand__mark{background:var(--navy)}
  .brand__name{font-family:"Poppins",sans-serif;font-weight:700;color:var(--ink);text-transform:uppercase;line-height:1.2;letter-spacing:-.2px}
  .brand--large{left:45px;top:62px}
  .brand--large .brand__mark{width:62px;height:62px}
  .brand--large .brand__name{font-size:16.5px}
  .brand--small{left:43px;top:40px;gap:8px}
  .brand--small .brand__mark{width:34px;height:34px}
  .brand--small .brand__name{font-size:8.6px}

  /* cover */
  .cover-title{position:absolute;left:47px;top:376px;border-left:5px solid var(--navy);padding-left:24px;font-family:"Poppins",sans-serif;font-weight:700;font-size:42px;line-height:46px;color:var(--navy);letter-spacing:-.5px}
  .cover-title__first{color:var(--ink)}
  .mod-date{position:absolute;left:45px;top:518px;width:442px;height:33px;background:var(--gold);color:var(--ink);font-family:"Poppins",sans-serif;font-weight:600;font-size:26px;line-height:34px;text-align:center;letter-spacing:.3px}
  .contact-line{position:absolute;display:flex;align-items:flex-end;font-size:11.5px;color:#444}
  .contact-line span.fill{display:block;border-bottom:1px solid #bbb;margin-left:8px;height:10px}
  .cover-swoosh{position:absolute;left:0;bottom:0}

  /* shared text */
  .para{position:absolute;left:43px;width:472px;font-size:8.8px;line-height:10.5px;letter-spacing:-.1px;color:var(--text)}
  .tick{position:relative;display:inline-block;width:10px;height:10px;border-radius:50%;background:var(--gold);flex:none;margin-top:0}
  .tick::after{content:"";position:absolute;left:3.4px;top:1.8px;width:2.6px;height:4.8px;border:solid var(--white);border-width:0 1.5px 1.5px 0;transform:rotate(45deg)}
  .tick-item{display:flex;gap:8px;font-weight:700;font-size:9.4px;line-height:10px}

  .tab{position:absolute;color:var(--white);font-family:"Poppins",sans-serif;font-weight:600;text-transform:uppercase;padding-left:8px;line-height:21px;font-size:13px;letter-spacing:.4px}
  .tab--gold{background:var(--gold);clip-path:polygon(0 0,88% 0,100% 100%,0 100%);padding-left:16px}
  .tab--navy{background:var(--navy);clip-path:polygon(0 0,94% 0,100% 100%,0 100%)}

  .factor-box{position:absolute;left:43px;top:155px;width:475px;height:84px;background:var(--navy);color:var(--white);display:grid;grid-template-columns:219px 1fr;padding:13px 0 0 16px;row-gap:8px}

  .callout{position:absolute;left:43px;top:257px;font-weight:700;font-size:10.6px;line-height:13.5px;color:var(--ink)}
  .callout em{font-style:normal;color:var(--navy)}

  .rule-list{position:absolute;color:var(--ink)}
  .rule-list .tick-item{margin-bottom:12px}

  .photo{position:absolute}
  .photo--office{left:43px;top:493px;width:465px;height:162px;background:linear-gradient(90deg,#b9a08c 0%,#d9d2c9 35%,#c7ccd2 60%,#eef0f2 100%)}
  .photo--handshake{left:46px;top:91px;width:480px;height:162px;background:linear-gradient(90deg,#5b7891 0%,#a9bccb 35%,#e8c9a1 52%,#a9bccb 68%,#4e6d88 100%);box-shadow:0 2px 6px rgba(0,0,0,.15)}

  .disclaimer{position:absolute;left:43px;width:470px;color:var(--ink)}
  .disclaimer h4{font-size:7.5px;font-weight:700;margin-bottom:5px}
  .disclaimer p{font-size:6.1px;line-height:8px;color:#444}

  /* mod page */
  .hr{position:absolute;left:43px;width:494px;height:1px;background:var(--rule)}
  .mod-meter{position:absolute;left:251px;top:313px;width:278px;height:16px;border-radius:8px;background:#d6d6d6}
  .mod-meter__fill{position:absolute;left:53px;width:152px;top:0;bottom:0;background:var(--navy)}
  .mod-meter__tick{position:absolute;left:150px;top:0;width:1px;height:16px;background:#3a4f92}
  .knob{position:absolute;top:-3px;width:22px;height:22px;border-radius:50%;border:2px solid var(--white);box-shadow:0 1px 3px rgba(0,0,0,.3)}
  .knob--min{left:42px;background:radial-gradient(circle,#d9a425 40%,#b78a18 100%)}
  .knob--actual{left:194px;background:radial-gradient(circle,#2b4fc2 40%,var(--navy) 100%)}
  .meter-label{position:absolute;font-size:8.6px;font-weight:700;line-height:10px;text-align:center;color:var(--ink)}

  .explain-box{position:absolute;left:43px;top:389px;width:481px;height:151px;background:var(--panel)}
  .explain-item{position:absolute;left:19px;width:420px;font-size:8.6px;line-height:10.5px;letter-spacing:-.1px;color:var(--text)}
  .explain-rule{position:absolute;left:19px;width:446px;height:1px;background:#bdbdbd}

  .summary-title{position:absolute;left:43px;top:555px;font-family:"Poppins",sans-serif;font-weight:600;font-size:14px;color:var(--ink);letter-spacing:.3px}
</style>
</head>
<body>

<!-- Cover -->
<section class="page page--cover">
  <div class="brand brand--large">
    <span class="brand__mark"></span>
    <span class="brand__name">Workers Compensation<br>Executive Summary</span>
  </div>
  <h1 class="cover-title"><span class="cover-title__first">WORKERS</span><br>COMPENSATION<br>EXECUTIVE SUMMARY</h1>
  <div class="mod-date">Mod Effective 10-08-2022</div>
  <div class="contact-line" style="left:45px;top:607px">Name of agent<span class="fill" style="width:356px"></span></div>
  <div class="contact-line" style="left:45px;top:638px">Phone no.<span class="fill" style="width:148px;margin-right:8px"></span>Email<span class="fill" style="width:190px"></span></div>
  <svg class="cover-swoosh" width="559" height="22" viewBox="0 0 559 22">
    <path d="M470 22 C490 8 505 2 520 4 C530 6 535 14 500 22 Z" fill="var(--gold)"/>
    <path d="M0 3 H465 C490 3 500 10 505 22 H0 Z" fill="var(--navy)"/>
  </svg>
</section>

<!-- Informative page -->
<section class="page page--intro">
  <div class="brand brand--small">
    <span class="brand__mark"></span>
    <span class="brand__name">Workers Compensation<br>Executive Summary</span>
  </div>
  <p class="para" style="top:92px">Workers compensation claims can have a significant impact on a business. In addition to the direct claim costs, there are many other costs associated with a workers compensation claim that can impact a business.</p>

  <div class="tab tab--gold" style="left:43px;top:134px;width:128px">They Are</div>
  <div class="factor-box">
    <div class="tick-item"><span class="tick"></span>Work Comp Premium Costs</div>
    <div class="tick-item"><span class="tick"></span>Lost Opportunities due to staffing</div>
    <div class="tick-item"><span class="tick"></span>Overtime</div>
    <div class="tick-item"><span class="tick"></span>Lost Productivity</div>
    <div class="tick-item"><span class="tick"></span>Administrative time spent on<br>claim after an injury</div>
    <div class="tick-item"><span class="tick"></span>Clean up or repair of damaged<br>equipment</div>
  </div>

  <p class="callout"><em>OSHA estimates that depending upon the size of the claim indirect</em><br>costs range from 1 to 4 times the direct costs.</p>
  <p class="para" style="top:289px">Workers compensation claims can have a significant impact on a business. In addition to the direct claim costs, there are many other costs associated with a workers compensation claim that can impact a business.</p>

  <div class="rule-list" style="left:43px;top:330px;width:220px">
    <div class="tick-item"><span class="tick"></span>A medical only claim is reduced by<br>70% in the mod calculation.</div>
    <div class="tick-item" style="margin-top:10px"><span class="tick"></span>A medical/indemnity claim has<br>no reduction.</div>
  </div>
  <div class="rule-list" style="left:282px;top:330px;width:230px">
    <div class="tick-item"><span class="tick"></span>All claims are also limited by a primary<br>threshold value where claims are<br>grouped into primary claims and<br>excess claims.</div>
  </div>

  <p class="para" style="top:401px">The following report will analyze the types of claims that are occurring in your business and will group them together for ease of identifying trends and areas of opportunity to improve.</p>
  <p class="para" style="top:434px">By identifying the types and causes of losses many times a cost/benefit analysis can be performed to allow for safety training, additional equipment or building or process improvements.</p>
  <p class="para" style="top:467px">For the premium cost analysis in this report we have used a manual premium of $XXX,XXX. A manual premium is the premium derived by the carrier before any credits, debits, or experience rating.</p>

  <div class="photo photo--office" role="img" aria-label="Photo of a team working at desks in a bright open-plan office"></div>

  <div class="disclaimer" style="top:668px">
    <h4>DISCLAIMER</h4>
    <p>Lorem Ipsum is simply dummy text of the printing and typesetting industry. Lorem Ipsum has been the industry's standard<br>dummy text ever since the 1500s, when an unknown printer took a galley of type.</p>
  </div>
  <div class="footer-band"></div>
</section>

<!-- Experience mod page -->
<section class="page page--mod">
  <div class="brand brand--small" style="top:36px">
    <span class="brand__mark"></span>
    <span class="brand__name">Workers Compensation<br>Executive Summary</span>
  </div>
  <div class="photo photo--handshake" role="img" aria-label="Photo of a business handshake over a city skyline"></div>

  <div class="hr" style="top:280px"></div>
  <div class="tab tab--navy" style="left:43px;top:281px;width:196px">Your Experience Mod</div>
  <p class="para" style="top:315px;width:200px">The report below shows your company's actual experience mod as wellas your lowest possible mod.</p>

  <div class="meter-label" style="left:430px;top:291px;width:55px">Actual Mod<br>1.19</div>
  <div class="mod-meter">
    <div class="mod-meter__fill"></div>
    <div class="mod-meter__tick"></div>
    <span class="knob knob--min"></span>
    <span class="knob knob--actual"></span>
  </div>
  <div class="meter-label" style="left:278px;top:342px;width:52px">0.63<br>Min Mod</div>
  <div class="hr" style="top:369px"></div>

  <div class="explain-box">
    <div class="explain-item" style="top:42px">A mod value below 1.0 means your company is performing better than yolur peers. If your company had no claims your lowest possible mod value would be 0.632</div>
    <div class="explain-rule" style="top:68px"></div>
    <div class="explain-item" style="top:84px">A mod of 1.0 is considered average.</div>
    <div class="explain-rule" style="top:102px"></div>
    <div class="explain-item" style="top:117px">A mod value above 1.0 means your company is performing worse than your peers and you pay more in workers compensation premium.</div>
  </div>
  <div class="tab tab--navy" style="left:43px;top:389px;width:221px">Mod Value Explanation</div>

  <h2 class="summary-title">SUMMARY</h2>
  <p class="para" style="top:584px">The incurred claims reported have a claim impact of .56 on your mod value.&nbsp; This is increasing your premium annually by $112,000.</p>
  <p class="para" style="top:617px">In the following pages we'll dig into the types of claims your business is having and look for areas of opportunity to reduce or eliminate claims and lower your mod value.</p>
  <div class="hr" style="top:653px"></div>

  <div class="disclaimer" style="top:668px">
    <h4>DISCLAIMER</h4>
    <p>Lorem Ipsum is simply dummy text of the printing and typesetting industry. Lorem Ipsum has been the industry's standard<br>dummy text ever since the 1500s, when an unknown printer took a galley of type.</p>
  </div>
  <div class="footer-band"></div>
</section>

</body>
</html>
```